Modern business card for triathlon training business in Australia

We need a business card design for our triathlon training company.

Lakeshore Pace Fitness is an Australian business, owned by women, run for women. Lakeshore Pace Fitness helps women prepare or improve triathlon skills and confidence through triathlon camps completely designed for women.

Our camps focus on preparing women both physically and mentally for their next (or first!) triathlon.

You can see our website www.lakeshorepacefitness.com.au for more info about our business and our style.

We've attached two of our logos and are happy to consider a design that utilised either colour scheme with the teal colour being our 'feature' colour. We don't want overly feminine cards but rather cards that are professional and neat. If the inclusion of any pictures/art is warranted, this should be focused on our swim/ride/run theme and in that specific order (swim/ride/run).

The business card needs to be a printable design and the contact details will need to change for our two employees.

Target Market(s)

Female clients and partners/vendors/sponsors that we work with in the triathlon industry

Industry/Entity Type

Fitness

Contact Information for Business Card

Lakeshore Pace Fitness (business name)
Maren Dunley
Business Director
Mobile: 0455 918 237
Email: maren@lakeshorepacefitness.com.au
www.lakeshorepacefitness.com.au

Second business card:
Lakeshore Pace Fitness
Bea Calvert
Coaching Director
Mobile: 0433 206 519
Email: bea@lakeshorepacefitness.com.au

Font styles to use
Serif
Sans Serif

Requirements
Must have
• Core contact details above, our logo and be a printable design
Should not have
• Pink
• Cursive/script fonts

```html
<!DOCTYPE html>
<html lang="en">
<head>
<meta charset="utf-8">
<title>Lakeshore Pace Fitness — Business Card</title>
<link href="https://fonts.googleapis.com/css2?family=Roboto+Condensed:wght@300;400;700&display=swap" rel="stylesheet">
<style>
  :root {
    --page-bg: #efe6d6;
    --card-black: #050505;
    --logo-panel: #111111;
    --teal: #1eb3cf;
    --teal-dark: #138aa0;
    --ink: #0a0a0a;
    --white: #ffffff;
  }
  * { margin: 0; padding: 0; box-sizing: border-box; }
  html, body {
    width: 1200px; height: 1000px; overflow: hidden;
    background: var(--page-bg);
    font-family: "Roboto Condensed", "Arial Narrow", sans-serif;
  }
  .business-card {
    position: absolute; left: 150px; top: 243px;
    width: 900px; height: 514px;
    background: var(--card-black);
    box-shadow: 0 18px 40px rgba(0,0,0,0.25);
    overflow: hidden;
  }
  .brand-block {
    position: absolute; left: 40px; top: 36px;
    width: 230px; height: 150px;
    background: var(--logo-panel);
    display: flex; align-items: center; justify-content: center;
    padding: 0 18px;
  }
  .brand-name {
    color: var(--teal);
    font-weight: 700; font-size: 30px; line-height: 1.05;
    text-transform: uppercase; text-align: center; letter-spacing: 0.5px;
  }
  .discipline-photo {
    position: absolute; top: 68px;
    width: 128px; height: 128px; border-radius: 50%;
  }
  .discipline-photo.swim { left: 340px; background: radial-gradient(circle at 40% 40%, #9fd3ea, #2b5fa8 70%, #1c3f7a); }
  .discipline-photo.ride { left: 500px; background: radial-gradient(circle at 55% 40%, #d7c7b8, #5c7fa6 60%, #3b8f8a); }
  .discipline-photo.run  { left: 660px; background: radial-gradient(circle at 50% 45%, #d9d26a, #8a8f5e 55%, #4d4a3c); }
  .name-ribbon { position: absolute; left: 0; top: 222px; width: 360px; height: 150px; }
  .person-name {
    position: absolute; left: 95px; top: 226px;
    font-size: 42px; font-weight: 400; color: var(--ink);
  }
  .person-role {
    position: absolute; left: 80px; top: 290px;
    font-size: 23px; font-weight: 400; color: var(--ink);
  }
  .contact-list {
    position: absolute; right: 40px; top: 340px;
    list-style: none; text-align: right; color: var(--teal);
  }
  .contact-list li {
    display: flex; align-items: center; justify-content: flex-end; gap: 12px;
    font-size: 23px; font-weight: 300; margin-bottom: 10px;
  }
  .contact-list li.phone { font-size: 36px; font-weight: 400; margin-bottom: 8px; }
  .contact-icon { width: 22px; height: 22px; flex: none; }
</style>
</head>
<body>
  <main class="business-card">
    <div class="brand-block"><span class="brand-name">Lakeshore Pace Fitness</span></div>

    <div class="discipline-photo swim" role="img" aria-label="Photo of a swimmer in cap and goggles"></div>
    <div class="discipline-photo ride" role="img" aria-label="Photo of a cyclist in helmet"></div>
    <div class="discipline-photo run" role="img" aria-label="Photo of a runner in sunglasses"></div>

    <svg class="name-ribbon" viewBox="0 0 360 150" aria-hidden="true">
      <polygon points="0,0 335,0 335,62 0,62" fill="var(--teal)"/>
      <polygon points="0,68 305,68 355,132 305,108 0,108" fill="var(--teal)"/>
      <polygon points="305,108 355,132 305,100" fill="var(--teal-dark)"/>
    </svg>
    <h1 class="person-name">Maren Dunley</h1>
    <p class="person-role">Business Director</p>

    <ul class="contact-list">
      <li class="phone">0455 918 237
        <svg class="contact-icon" viewBox="0 0 24 24" aria-hidden="true"><rect x="4" y="2" width="16" height="20" rx="2" fill="none" stroke="var(--teal)" stroke-width="2"/><circle cx="12" cy="18" r="1.2" fill="var(--teal)"/></svg>
      </li>
      <li class="email">maren@lakeshorepacefitness.com.au
        <svg class="contact-icon" viewBox="0 0 24 24" aria-hidden="true"><rect x="2" y="5" width="20" height="14" fill="none" stroke="var(--teal)" stroke-width="2"/><polyline points="2,5 12,13 22,5" fill="none" stroke="var(--teal)" stroke-width="2"/></svg>
      </li>
      <li class="web">www.lakeshorepacefitness.com.au
        <svg class="contact-icon" viewBox="0 0 24 24" aria-hidden="true"><circle cx="12" cy="12" r="9" fill="none" stroke="var(--teal)" stroke-width="2"/><ellipse cx="12" cy="12" rx="4" ry="9" fill="none" stroke="var(--teal)" stroke-width="1.5"/><line x1="3" y1="12" x2="21" y2="12" stroke="var(--teal)" stroke-width="1.5"/></svg>
      </li>
    </ul>
  </main>
</body>
</html>
```